Realtor business card

Looking for a business card that will stand out from the rest. My area of expertise is residential real estate and loans.

Industry/Entity Type

Residential

Requirements
Must have
• Marcus Whitley, SFR
Broker
Mortgage Loan Originator
Notary Public
DRE License #07329184
NMLS 581706
Cell 714-552-0718
Fax 888-417-2965
www.marcuswhitleyhomes.example
mw@marcuswhitleyhomes.example

```html
<!DOCTYPE html>
<html lang="en">
<head>
<meta charset="utf-8">
<title>Marcus Whitley – Business Card</title>
<link rel="stylesheet" href="https://fonts.googleapis.com/css2?family=Cinzel:wght@400&family=Open+Sans:wght@400&display=swap">
<style>
  :root {
    --charcoal: #3b3b3c;
    --black: #000000;
    --gold: #f5ea14;
    --white: #ffffff;
  }
  html, body {
    margin: 0;
    padding: 0;
    overflow: hidden;
    background: var(--white);
  }
  .card {
    position: relative;
    width: 1200px;
    height: 695px;
    overflow: hidden;
    background: var(--black);
  }
  .block { position: absolute; }
  .block--top-left { left: 0; top: 0; width: 600px; height: 345px; background: var(--charcoal); }
  .block--top-right { left: 600px; top: 0; width: 600px; height: 349px; background: var(--black); }
  .block--bottom-left { left: 0; top: 345px; width: 600px; height: 350px; background: var(--black); }
  .block--bottom-right { left: 600px; top: 349px; width: 600px; height: 346px; background: var(--charcoal); }

  .identity {
    position: absolute;
    left: 625px;
    top: 283px;
    transform: translateX(-50%);
    text-align: center;
    white-space: nowrap;
  }
  .identity__name {
    margin: 0;
    font-family: "Cinzel", "Copperplate", serif;
    font-weight: 400;
    font-size: 74px;
    line-height: 1;
    letter-spacing: 1px;
    color: var(--gold);
  }
  .identity__roles {
    margin: 6px 0 0;
    font-family: "Open Sans", Arial, sans-serif;
    font-size: 27px;
    line-height: 1.2;
    color: var(--white);
  }
</style>
</head>
<body>
  <main class="card">
    <div class="block block--top-left"></div>
    <div class="block block--top-right"></div>
    <div class="block block--bottom-left"></div>
    <div class="block block--bottom-right"></div>

    <div class="identity">
      <h1 class="identity__name">Marcus Whitley</h1>
      <p class="identity__roles">SFR Broker Mortgage Loan Originator Notary Public</p>
    </div>
  </main>
</body>
</html>
```